The Lantern and the Meadow: Songs Of Quiet Bloom

We need a book cover/spine and back cover for a multi author book called the Lantern and The Meadow: Songs of Quiet Bloom. This will be a collection of stories from women who major transformational stories to tell. They embark on a voyage, find themselves in uncharted territory, find friends or allies and in the end find themselves back home to themselves. I want this book cover to feel fun of wonder, adventure, intrigue with a a dainty energy. I have uploaded some images for inspiration but not to use in the design because they are not images I have permission to use.

```html
<!DOCTYPE html>
<html lang="en">
<head>
<meta charset="utf-8">
<title>The Lantern and the Meadow: Songs of Quiet Bloom — Front Cover</title>
<link rel="stylesheet" href="https://fonts.googleapis.com/css2?family=Bebas+Neue&family=EB+Garamond:wght@400&family=Oswald:wght@400&display=swap">
<style>
  :root {
    --backdrop: #2b2b2b;
    --teal: #3f9caa;
    --pink: #ee2c8a;
    --white: #ffffff;
    --sky-top: #d6eef8;
    --sky-mid: #eef8fc;
    --horizon: #fffdf9;
    --glow: #f8dcc3;
    --sun: rgba(255, 250, 225, 0.95);
    --haze: #c9b7c4;
    --ridge-light: #a99cb6;
    --ridge-dark: #716783;
    --hill: #5e5062;
    --meadow: #4f5a31;
    --meadow-deep: #2c3820;
    --bloom: rgba(214, 64, 160, 0.55);
    --bloom-soft: rgba(230, 96, 180, 0.35);
  }
  html, body {
    margin: 0;
    width: 1200px;
    height: 1200px;
    overflow: hidden;
    background: var(--backdrop);
  }
  .cover {
    position: absolute;
    left: 295px;
    top: 137px;
    width: 609px;
    height: 914px;
    overflow: hidden;
  }
  .cover-photo {
    position: absolute;
    inset: 0;
    background:
      radial-gradient(ellipse 40% 12% at 74% 62%, var(--sun) 0%, rgba(255, 240, 215, 0) 100%),
      radial-gradient(ellipse 45% 14% at 20% 86%, var(--bloom) 0%, rgba(214, 64, 160, 0) 100%),
      radial-gradient(ellipse 40% 12% at 82% 92%, var(--bloom) 0%, rgba(214, 64, 160, 0) 100%),
      radial-gradient(ellipse 35% 10% at 55% 98%, var(--bloom-soft) 0%, rgba(230, 96, 180, 0) 100%),
      radial-gradient(ellipse 30% 8% at 12% 96%, var(--bloom-soft) 0%, rgba(230, 96, 180, 0) 100%),
      linear-gradient(174deg, rgba(0, 0, 0, 0) 0%, rgba(0, 0, 0, 0) 76%, var(--meadow) 79%, var(--meadow-deep) 100%),
      linear-gradient(
        to bottom,
        var(--sky-top) 0%,
        var(--sky-mid) 30%,
        var(--horizon) 50%,
        var(--glow) 60%,
        var(--haze) 64%,
        var(--ridge-light) 68%,
        var(--ridge-dark) 74%,
        var(--hill) 82%,
        var(--hill) 100%
      );
  }
  .cover-type {
    position: absolute;
    inset: 0;
    width: 100%;
    height: 100%;
  }
  .title-word { font-family: "Bebas Neue", sans-serif; }
  .title-top { fill: var(--teal); }
  .title-bottom { fill: var(--pink); }
  .title-joiner { font-family: "Bebas Neue", sans-serif; fill: var(--teal); }
  .title-rule { stroke: var(--teal); stroke-width: 4; }
  .subtitle { font-family: "EB Garamond", serif; fill: var(--white); font-size: 36px; }
  .author { font-family: "Oswald", sans-serif; font-weight: 400; fill: var(--white); font-size: 48px; }
</style>
</head>
<body>
  <div class="cover">
    <div class="cover-photo" role="img" aria-label="Photograph of a woman seen from behind with arms raised on a hillside meadow of pink flowers, facing a sunrise over layered misty mountain ridges"></div>
    <svg class="cover-type" viewBox="0 0 609 914" xmlns="http://www.w3.org/2000/svg">
      <text class="title-word title-top" x="65" y="209" font-size="226" textLength="483" lengthAdjust="spacingAndGlyphs">LANTERN</text>
      <line class="title-rule" x1="65" y1="252" x2="197" y2="252"/>
      <line class="title-rule" x1="414" y1="252" x2="548" y2="252"/>
      <text class="title-joiner" x="220" y="276" font-size="67" textLength="171" lengthAdjust="spacingAndGlyphs">AND THE</text>
      <text class="title-word title-bottom" x="64" y="442" font-size="213" textLength="484" lengthAdjust="spacingAndGlyphs">MEADOW</text>
      <text class="subtitle" x="305" y="796" text-anchor="middle">Songs of Quiet Bloom</text>
      <text class="author" x="105" y="886" textLength="401" lengthAdjust="spacing">AUTHOR NAME</text>
    </svg>
  </div>
</body>
</html>
```